Brackenmoor Lane School bookmark

We need a vertical card (DL 99x210 mm) that will be put inside books at a primary school for children to make comments about the books. Text at the top:
Brackenmoor Lane School (and logo)
What did you think of this book?

Text at the bottom:
Pass it on!

Words in repeated pattern around the edge: funny sad exciting mysterious fantastic boring enthralling interesting

It should be in interesting bright colours with a white or pale background as children will write on the cards

The card should be double sided with the same design on each side

```html
<!DOCTYPE html>
<html lang="en">
<head>
<meta charset="utf-8">
<title>Brackenmoor Lane School bookmark</title>
<link rel="stylesheet" href="https://fonts.googleapis.com/css2?family=Arimo:wght@700&family=Mali:ital,wght@1,500&family=Open+Sans:wght@300&family=Righteous&display=swap">
<style>
  :root {
    --page: #f1efec;
    --border-band: #c6e3e1;
    --panel: #e3e3d9;
    --panel-guide: #2f6fd1;
    --border-word: #ffffff;
    --title: #5e6166;
    --tab-pink: #f08aa4;
    --tab-stitch: #8b5a66;
    --write-line: #a9a99b;
    --bubble: #ffffff;
    --bubble-stitch: #b9d8dc;
    --bubble-text: #6a6a6a;
    --art-teal: #9fcfd2;
    --art-warm: #e9c4b4;
    --art-branch: #cfcab6;
    --pass-red: #e8262c;
  }
  * { box-sizing: border-box; margin: 0; padding: 0; }
  html, body { width: 1137px; height: 1200px; overflow: hidden; }
  body { background: var(--page); position: relative; }

  .bookmark {
    position: absolute;
    top: 112px;
    width: 460px;
    height: 976px;
    background: var(--border-band);
    box-shadow: 0 2px 6px rgba(0,0,0,.18);
  }
  .bookmark--front { left: 76px; }
  .bookmark--back { left: 601px; }

  .word-border { position: absolute; inset: 0; width: 460px; height: 976px; }
  .word-border text {
    font-family: "Mali", cursive;
    font-style: italic;
    font-weight: 500;
    font-size: 15px;
    fill: var(--border-word);
    letter-spacing: .5px;
  }
  .word-border .pass-it-on {
    font-family: "Righteous", sans-serif;
    font-style: normal;
    font-size: 25px;
    fill: var(--pass-red);
    letter-spacing: 2px;
  }

  .writing-panel {
    position: absolute;
    left: 50px; top: 44px;
    width: 371px; height: 887px;
    background: var(--panel);
    outline: 1px dashed var(--panel-guide);
  }

  .school-mark {
    position: absolute;
    left: 16px; top: 3px;
    width: 134px; height: 134px;
    border-radius: 50%;
    background: #ffffff;
  }
  .school-name {
    position: absolute;
    left: 168px; top: 40px;
    width: 200px;
    font-family: "Arimo", sans-serif;
    font-weight: 700;
    font-size: 25px;
    line-height: 33px;
    color: var(--title);
    text-align: center;
  }

  .comment-tab {
    position: absolute;
    left: -3px; top: 161px;
    width: 55px; height: 256px;
    border-radius: 0 26px 26px 0;
    background: var(--tab-pink);
  }
  .comment-tab::after {
    content: "";
    position: absolute;
    inset: 7px 7px 7px -2px;
    border: 1.5px dashed var(--tab-stitch);
    border-left: none;
    border-radius: 0 20px 20px 0;
  }

  .comment-lines {
    position: absolute;
    left: 68px; top: 142px;
    width: 254px;
    list-style: none;
  }
  .comment-lines li {
    height: 40px;
    border-bottom: 3px dotted var(--write-line);
  }

  .question-bubble {
    position: absolute;
    left: 157px; top: 440px;
    width: 206px; height: 153px;
  }
  .question-bubble svg { position: absolute; inset: 0; }
  .question-text {
    position: absolute;
    left: 40px; top: 30px;
    width: 140px;
    font-family: "Open Sans", sans-serif;
    font-weight: 300;
    font-size: 15px;
    line-height: 22px;
    color: var(--bubble-text);
    text-align: center;
    transform: rotate(8deg);
  }

  .owl-illustration {
    position: absolute;
    left: 5px; top: 606px;
    width: 362px; height: 276px;
    border-radius: 6px;
    background: linear-gradient(180deg, var(--art-teal) 0%, var(--art-warm) 65%, var(--art-branch) 100%);
  }
</style>
</head>
<body>

<article class="bookmark bookmark--front">
  <svg class="word-border" viewBox="0 0 460 976" aria-hidden="true">
    <text x="48" y="32">mysterious</text>
    <text x="168" y="32">fantastic</text>
    <text x="270" y="32">boring</text>
    <text x="346" y="32">enthralling</text>
    <text transform="translate(31,968) rotate(-90)" textLength="868" lengthAdjust="spacing">funny sad exciting mysterious fantastic boring enthralling interesting funny sad exciting</text>
    <text transform="translate(446,968) rotate(-90)" textLength="868" lengthAdjust="spacing">funny sad exciting mysterious fantastic boring enthralling interesting funny sad exciting</text>
    <text x="56" y="960">mysterious</text>
    <text x="176" y="960">fantastic</text>
    <text class="pass-it-on" x="262" y="962">PASS IT ON!</text>
  </svg>
  <div class="writing-panel">
    <div class="school-mark"></div>
    <h1 class="school-name">Brackenmoor Lane School</h1>
    <div class="comment-tab"></div>
    <ul class="comment-lines"><li></li><li></li><li></li><li></li><li></li><li></li><li></li></ul>
    <div class="question-bubble">
      <svg viewBox="0 0 206 153" aria-hidden="true">
        <path d="M40 108 C12 108 4 80 22 66 C10 44 34 22 58 30 C70 8 108 6 122 24 C142 10 176 22 176 46 C200 52 204 86 184 98 C186 122 158 132 138 120 C124 136 96 134 86 120 L58 148 L64 114 C54 114 46 112 40 108 Z" fill="var(--bubble)"/>
        <path d="M44 100 C22 98 16 80 30 70 C20 50 40 34 60 40 C72 20 104 18 118 34 C136 22 166 32 166 52 C186 58 190 84 174 92 C176 112 154 120 138 110 C124 124 100 122 90 110" fill="none" stroke="var(--bubble-stitch)" stroke-width="1.2" stroke-dasharray="3 3"/>
      </svg>
      <p class="question-text">What<br>did you think<br>of this book?</p>
    </div>
    <div class="owl-illustration" role="img" aria-label="Illustration area: cartoon owl sitting on a tree branch"></div>
  </div>
</article>

<article class="bookmark bookmark--back">
  <svg class="word-border" viewBox="0 0 460 976" aria-hidden="true">
    <text x="48" y="32">mysterious</text>
    <text x="168" y="32">fantastic</text>
    <text x="270" y="32">boring</text>
    <text x="346" y="32">enthralling</text>
    <text transform="translate(31,968) rotate(-90)" textLength="868" lengthAdjust="spacing">funny sad exciting mysterious fantastic boring enthralling interesting funny sad exciting</text>
    <text transform="translate(446,968) rotate(-90)" textLength="868" lengthAdjust="spacing">funny sad exciting mysterious fantastic boring enthralling interesting funny sad exciting</text>
    <text x="56" y="960">mysterious</text>
    <text x="176" y="960">fantastic</text>
    <text class="pass-it-on" x="262" y="962">PASS IT ON!</text>
  </svg>
  <div class="writing-panel">
    <div class="school-mark"></div>
    <h2 class="school-name">Brackenmoor Lane School</h2>
    <div class="comment-tab"></div>
    <ul class="comment-lines"><li></li><li></li><li></li><li></li><li></li><li></li><li></li></ul>
    <div class="question-bubble">
      <svg viewBox="0 0 206 153" aria-hidden="true">
        <path d="M40 108 C12 108 4 80 22 66 C10 44 34 22 58 30 C70 8 108 6 122 24 C142 10 176 22 176 46 C200 52 204 86 184 98 C186 122 158 132 138 120 C124 136 96 134 86 120 L58 148 L64 114 C54 114 46 112 40 108 Z" fill="var(--bubble)"/>
        <path d="M44 100 C22 98 16 80 30 70 C20 50 40 34 60 40 C72 20 104 18 118 34 C136 22 166 32 166 52 C186 58 190 84 174 92 C176 112 154 120 138 110 C124 124 100 122 90 110" fill="none" stroke="var(--bubble-stitch)" stroke-width="1.2" stroke-dasharray="3 3"/>
      </svg>
      <p class="question-text">What<br>did you think<br>of this book?</p>
    </div>
    <div class="owl-illustration" role="img" aria-label="Illustration area: cartoon owl sitting on a tree branch"></div>
  </div>
</article>

</body>
</html>
```